Webdesign für lokalen Dart-Shop
Zielgruppe
Wir sind ein lokaler Dart-Shop in Hamburg, welcher in Norddeutschland sehr beliebt ist und bundesweit das Größte Angebot bietet. Durch unseren Online-Shop möchte wir unseren Radius erweitern.
Zielgruppe: Dart Anfänger, Fortgeschrittene sowie Vereine und Unternehmen
Aufgabenstellung
In jedem Fall das Haupt-Element unseres Logo´s, einer Dart-Scheibe.

```html
<!DOCTYPE html>
<html lang="de">
<head>
<meta charset="utf-8">
<title>Pfeilhaus Nord – News</title>
<link href="https://fonts.googleapis.com/css2?family=Roboto:wght@400;500&family=Jost:wght@400;500&display=swap" rel="stylesheet">
<style>
  :root {
    --black: #000000;
    --page-grey: #f2f2f2;
    --white: #ffffff;
    --red: #e8242a;
    --nav-red: #b23a3a;
    --text: #333333;
    --footer-text: #ffffff;
    --footer-red: #e8242a;
  }
  * { margin: 0; padding: 0; box-sizing: border-box; }
  html, body { width: 1200px; height: 800px; overflow: hidden; background: var(--black); }
  .site { width: 1200px; height: 800px; display: flex; flex-direction: column; }

  .site-header { height: 100px; position: relative; background: var(--black); }
  .brand { position: absolute; left: 312px; top: 18px; display: flex; align-items: center; gap: 10px; }
  .brand-mark { width: 58px; height: 58px; border-radius: 50%; background: #d9d9d9; }
  .brand-name { font-family: "Roboto", sans-serif; font-weight: 500; font-size: 13px; color: var(--white); letter-spacing: .04em; }
  .main-nav { position: absolute; left: 520px; top: 79px; display: flex; gap: 0; }
  .main-nav a { font-family: "Roboto", sans-serif; font-size: 8.5px; color: var(--white); text-decoration: none; padding: 4px 14px; height: 17px; display: block; }
  .main-nav a.is-active { background: var(--nav-red); padding: 4px 16px; margin-left: 4px; }

  .content-band { height: 420px; background: var(--page-grey); }
  .news-column { width: 602px; height: 100%; margin-left: 300px; background: var(--white); padding: 14px 10px 0 11px; }
  .notice { text-align: center; font-family: "Roboto", sans-serif; color: var(--red); font-size: 13.5px; line-height: 19.5px; }
  .notice + .notice { margin-top: 12px; }
  .notice strong { font-weight: 500; }
  .letter { font-family: "Roboto", sans-serif; font-size: 8.6px; line-height: 13px; color: var(--text); margin-top: 20px; }
  .letter p { margin-bottom: 13px; }
  .letter ol { margin: 0 0 13px 12px; }
  .letter li { padding-left: 2px; }
  .letter b { font-weight: 500; color: #111; }

  .site-footer { flex: 1; background: var(--black); position: relative; font-family: "Jost", sans-serif; font-size: 7.6px; line-height: 13px; color: var(--footer-text); }
  .footer-col { position: absolute; top: 12px; }
  .footer-col h3 { font-size: 8.2px; font-weight: 500; text-transform: uppercase; margin-bottom: 1px; }
  .footer-col h3.spaced { margin-top: 13px; }
  .footer-col ul { list-style: none; }
  .col-more { left: 332px; }
  .col-contact { left: 510px; }
  .col-route { left: 715px; width: 190px; }
  .col-route .address { color: var(--footer-red); }
</style>
</head>
<body>
<div class="site">
  <header class="site-header">
    <div class="brand">
      <span class="brand-mark"></span>
      <span class="brand-name">PFEILHAUS NORD</span>
    </div>
    <nav class="main-nav">
      <a href="#">Home</a>
      <a href="#">Shop</a>
      <a href="#" class="is-active">News</a>
    </nav>
  </header>

  <main class="content-band">
    <article class="news-column">
      <p class="notice">Ihr möchtet uns gerne unterstützen?<br>Unter folgender Adresse findet Ihr unseren neuen Online-<strong>Shop:</strong><br>https://shop.pfeilhaus-nord.de</p>
      <p class="notice">!!!WICHTIG!!!<br>Unser lokaler Shop ist vom 16.12.2020 - 14.02.<strong>2021 wegen der Corona</strong><br>Pandemie leider <strong>geschlossen!!!</strong></p>
      <div class="letter">
        <p>Liebe Pfeilhaus Nord Kunden,</p>
        <p>wir dürfen ab dem 20.04.2020 wieder öffnen!<br>Aufgrund der aktuellen Entwicklung des Corona-Virus wird es bis auf <b>weiteres folgenden Ablauf zum Eintritt in unseren Shop geben.</b></p>
        <ol>
          <li>Bitte klopfen, wenn die Tür verschlossen ist.</li>
          <li>Zur gleichen Zeit ist der Einlass von nur 4 Personen möglich.</li>
          <li>Pro Kunde müssen wir die Einkaufzeit leider auf maximal <b>15-30 Minuten limitieren, falls andere Kunden vor dem Pfeilhaus warten. Damit die</b> Warteschlange nicht zu groß wird.</li>
          <li>Für Euren sicheren Aufenthalt bei uns, halten wir <b>für Euch Einmalhandschuhe sowie Desinfektionsmittel kostenlos bereit!</b></li>
          <li>Bitte haltet wenn möglich im ganzen Shop einen <b>Mindestabstand von 1 - 1,5 Meter ein.</b></li>
          <li>Bitte wenn möglich Bargeldzahlung vermeiden.</li>
        </ol>
        <p>Alle wartenden Kunden können auf unseren <b>Bänken vor dem Pfeilhaus Platz nehmen und bekommen von uns gratis Kaffee oder Soft-Getränke!</b><br>Bitte achtet auch hier auf den Mindestabstand!</p>
        <p>Danke für Euer Verständnis und bleibt gesund. #dartswm #darts</p>
      </div>
    </article>
  </main>

  <footer class="site-footer">
    <section class="footer-col col-more">
      <h3>Mehr über</h3>
      <ul>
        <li>Impressum</li>
        <li>Kontakt</li>
        <li>Versand- &amp; Zahlungsbedingungen</li>
        <li>Widerrufsrecht &amp; Muster-Widerrufsformular</li>
        <li>AGB</li>
        <li>Privatsphäre und Datenschutz</li>
        <li>Callback Service</li>
      </ul>
    </section>
    <section class="footer-col col-contact">
      <h3>Kontakt</h3>
      <ul>
        <li>Tel: 040 555 123 40 - 0</li>
        <li>Fax: 040 555 123 40 - 9</li>
        <li>info@pfeilhaus-nord.de</li>
        <li>www.pfeilhaus-nord.de</li>
      </ul>
      <h3 class="spaced">Shop Öffnungszeiten</h3>
      <ul><li>Montag - Samstag 12:00 - 18:00</li></ul>
    </section>
    <section class="footer-col col-route">
      <h3>Anfahrt</h3>
      <ul class="address">
        <li>Pfeilhaus Nord GmbH</li>
        <li>Beispielweg 12</li>
        <li>20000 Hamburg</li>
      </ul>
      <p>Parkmöglichkeiten direkt vor dem Ladengeschäft oder in der Einbahnstraße, welche direkt um das Grundstück herum führt. S-Bahn Lindenplatz nur 200m entfernt!</p>
    </section>
  </footer>
</div>
</body>
</html>
```